Kestrel Bread Ingredients

Ingredients list/einkorn info. We are looking to improve a 5.5 x 8.5" double sided handout (2 per 8.5 x 11" piece of paper) to hand out with bread and for marketing. Or skinnier 3 per piece of paper? Or suggest a better format. Also to be used in social media and web. And possibly a banner.

Target Market(s)

Healthy, intelligent, yoga, athletic, wealthy

Industry/Entity Type

Bakery

Font styles to use
Sans Serif
Other font styles liked:
• simple readable attractive

Requirements
Must have
• Display the value (and uniqueness) of ingredients
Nice to have
• Well presented info with instant visual appeal. Choose between the 2 logos which you like most. Let us know if you want more photos.
Should not have
• Ornate frills

```html
<!DOCTYPE html>
<html lang="en">
<head>
<meta charset="utf-8">
<title>Kestrel Bread – Einkorn Handout</title>
<link rel="stylesheet" href="https://fonts.googleapis.com/css2?family=Noto+Serif:ital,wght@0,300;0,400;0,700;1,300;1,400;1,700&display=swap">
<style>
  :root {
    --ink-dark: #2e1c10;
    --ink-brown: #4a2a22;
    --ink-body: #4b3a33;
    --cream: #f1e8d6;
    --cream-soft: #efe4d2;
    --parchment: #c9a57c;
    --parchment-light: #dccab2;
    --wheat-gold: #c79a45;
    --wheat-deep: #8e6a2c;
    --crumb-light: #c58d5a;
    --crumb-dark: #8a5632;
    --seal: #ebe5dc;
    --credit: #8d8478;
  }
  * { margin: 0; padding: 0; box-sizing: border-box; }
  html, body { width: 927px; height: 1200px; overflow: hidden; background: #ffffff; }
  body { position: relative; font-family: "Noto Serif", Georgia, serif; }

  /* ---------- Front: Einkorn card ---------- */
  .einkorn-card {
    position: absolute; left: 162px; top: 74px; width: 596px; height: 487px;
    background: linear-gradient(100deg, var(--parchment) 0%, #cfae88 55%, var(--parchment-light) 100%);
    overflow: hidden; color: var(--ink-dark);
  }
  .wheat-photo {
    position: absolute; left: 405px; top: 0; width: 191px; height: 487px;
    background:
      radial-gradient(ellipse 40% 35% at 62% 62%, rgba(142,106,44,.85), rgba(199,154,69,.55) 60%, rgba(199,154,69,0) 100%),
      linear-gradient(180deg, rgba(214,178,100,.35) 0%, rgba(199,154,69,.45) 60%, rgba(120,85,35,.5) 100%);
  }
  .photo-credit {
    position: absolute; left: 573px; top: 294px; width: 150px;
    transform-origin: 0 0; transform: translate(18px, 0) rotate(90deg);
    font-size: 8px; color: var(--credit); font-family: "Noto Serif", serif; white-space: nowrap;
  }
  .einkorn-title {
    position: absolute; left: 34px; top: 78px;
    font-size: 38px; line-height: 36px; font-weight: 400; color: var(--ink-dark);
  }
  .einkorn-title em { font-style: italic; }
  .einkorn-lead {
    position: absolute; left: 34px; top: 167px;
    font-size: 15px; line-height: 18px; font-weight: 700; color: var(--cream-soft);
  }
  .einkorn-intro {
    position: absolute; left: 34px; top: 218px; font-size: 15px; font-weight: 400;
  }
  .einkorn-facts {
    position: absolute; left: 34px; top: 256px; width: 470px; list-style: none;
    font-size: 12.6px; line-height: 17.6px;
  }
  .einkorn-facts li { padding-left: 12px; position: relative; }
  .einkorn-facts li.bullet::before {
    content: ""; position: absolute; left: 1px; top: 7px; width: 5px; height: 5px;
    border-radius: 50%; background: var(--ink-dark);
  }
  .einkorn-note {
    position: absolute; left: 34px; top: 430px;
    font-size: 12.6px; font-style: italic; font-weight: 400;
  }

  /* ---------- Back: Transformation card ---------- */
  .bread-card {
    position: absolute; left: 158px; top: 595px; width: 604px; height: 494px; overflow: hidden;
    background:
      radial-gradient(ellipse 60% 55% at 62% 8%, #7c7b76 0%, rgba(124,123,118,0) 100%),
      radial-gradient(ellipse 55% 60% at 55% 60%, #b4a5a0 0%, rgba(180,165,160,0) 100%),
      linear-gradient(165deg, #c9b894 0%, #b09a80 45%, #a98c73 100%);
    color: var(--ink-body);
  }
  .bread-photo {
    position: absolute; left: 335px; top: 0; width: 269px; height: 494px;
    background: linear-gradient(160deg, var(--crumb-light) 0%, #a86e43 50%, var(--crumb-dark) 100%);
    clip-path: polygon(153px 0, 269px 0, 269px 494px, 62px 494px, 0 278px, 82px 212px, 76px 92px, 150px 40px);
  }
  .brand-seal {
    position: absolute; left: 442px; top: 334px; width: 120px; height: 120px; border-radius: 50%;
    background: var(--seal);
    display: flex; align-items: center; justify-content: center;
  }
  .brand-name { font-size: 14px; font-weight: 700; color: var(--ink-brown); }
  .bread-title {
    position: absolute; left: 28px; top: 36px;
    font-size: 33px; font-style: italic; font-weight: 300; color: var(--cream);
  }
  .bread-headline {
    position: absolute; left: 28px; top: 84px;
    font-size: 26px; font-weight: 700; color: var(--ink-brown); line-height: 30px;
  }
  .bread-tagline {
    position: absolute; left: 28px; top: 111px;
    font-size: 15px; font-style: italic; font-weight: 700; color: var(--ink-brown);
  }
  .ingredient-group {
    position: absolute; left: 28px; width: 330px;
    font-size: 13.4px; line-height: 17.6px; font-weight: 400; color: var(--ink-body);
  }
  .ingredient-group strong { color: var(--cream); font-weight: 700; font-size: 14.6px; }
  .group-grains { top: 140px; }
  .group-seeds { top: 204px; }
  .group-adaptogens { top: 268px; }
  .group-mushrooms { top: 296px; }
  .group-with { top: 325px; }
  .tolerance-note {
    position: absolute; left: 28px; top: 403px;
    font-size: 13px; line-height: 17px; font-weight: 300; color: var(--cream);
  }
  .contact {
    position: absolute; left: 28px; top: 450px;
    font-size: 17px; font-weight: 700; color: var(--ink-brown); word-spacing: 2px;
  }
</style>
</head>
<body>

  <section class="einkorn-card">
    <div class="wheat-photo" role="img" aria-label="Photograph of a bundle of golden einkorn wheat stalks with long awns, tied with twine"></div>
    <p class="photo-credit">Commons image: lnk.example/w4k</p>

    <h1 class="einkorn-title">Einkorn Grain<br><em>vs</em> ‘Modern Wheat’</h1>
    <p class="einkorn-lead">Einkorn is the original, non-altered wheat grain.<br>It's genetic purity is over 10,000 years old.</p>
    <p class="einkorn-intro">Einkorn is:</p>
    <ul class="einkorn-facts">
      <li class="bullet">25% higher in protein and lower in carbohydrates than modern wheat</li>
      <li class="bullet">3-4 times more beta-carotene</li>
      <li class="bullet">2 times more vitamin A</li>
      <li class="bullet">4 times more antioxidants lutein and riboflavin.</li>
      <li class="bullet">5-6 times more expensive $$$</li>
      <li class="bullet">Richer in carotenoids, B vitamins, and essential and trace minerals</li>
      <li>non-processed, non-hybridized, non-GMO, non-&nbsp;&nbsp; mutated and has a low glycemic load, meaning it won’t spike your blood sugar level.</li>
      <li>and it tastes better.</li>
    </ul>
    <p class="einkorn-note">Einkorn lacks the gluten proteins that trigger symptoms of gluten sensitivity.</p>
  </section>

  <section class="bread-card">
    <div class="bread-photo" role="img" aria-label="Photograph of stacked slices of marbled sprouted-grain bread"></div>
    <div class="brand-seal"><span class="brand-name">Kestrel Bread</span></div>

    <h2 class="bread-title">The Transformation of Bread</h2>
    <p class="bread-headline">Nutritious Digestible Delicious</p>
    <p class="bread-tagline">An alternative to the mutated genetics of modern wheat</p>

    <p class="ingredient-group group-grains"><strong>Sprouted grains</strong> Einkorn, spelt, and a touch of heritage rye (Organically grown on family farms in Winthrop, Washingtonand Teton Valley, Idaho)</p>
    <p class="ingredient-group group-seeds"><strong>Seeds</strong> Amaranth, sprouted pumpkin seeds, sprouted quinoa, chia seeds, flaxseed, hemp hearts, sprouted sunflowers seeds</p>
    <p class="ingredient-group group-adaptogens"><strong>Adaptogens</strong> Ashwaganda, Maca root</p>
    <p class="ingredient-group group-mushrooms"><strong>Mushroom extracts</strong> Lions mane, cordycept</p>
    <p class="ingredient-group group-with"><strong>With:</strong> Montana glacier well water, Cacao, MCT oil, psyilium husk, Himalayan sea salt, trace minerals, love</p>

    <p class="tolerance-note">This bread is well tolerated by people with<br>gluten sensitivities (not for celiac disease)</p>
    <p class="contact">hello@kestrelbread.com&nbsp; 406-555-0142</p>
  </section>

</body>
</html>
```